依頼詳細
構成は添付ファイルのとおりです。
ロゴはサイト名の公開ができないためとりあえず Rinkel Nexa でデザインをお願いいたします。
後日正式なものと入れ替えていただきますが、その際に多少調整をお願いする予定です。
サイトURL
ページ数
3ページ
希望イメージ
シンプル 複雑
単色 カラフル
暗い 明るい
日常 高級
遊び心 厳粛
未来的 伝統的
女性的 男性的
希望する色
青系、水色系
納品ファイル
• 高解像度JPG (.jpg)
補足説明
XDファイルでもOKです。
少々分かりづらい部分がありましたので追記です。

・右上トップメニューは例えばハンバーガーアイコンのようなものになるかと思います。
出会い掲示板以外のメニュー(チャットやコミュニティリンク集などへ移動できます)

・タイトル下部に投稿内容のプレビュー(1-2行程度)を表示願います。

・写真は添付がある投稿とない投稿があるため、ない場合においては写真の部分の余白を埋めてください。

・ページ2
プロフィール・ラベル・キーワード  3つのタブに別れた状態
と記載のある部分ですがPowerPointの資料においては「プロフィール」のタブが選択された状態を示しています
上部で3分割されて個々の検索条件をしていする作りですがコンペにおいては「プロフィール」タブが選択された状態にしておいてください。

「絞り込み検索結果の条件表示」の部分に指定した条件が表示され、どういう状態で抽出しているかが分かる仕組みです。

よろしくお願いいたします。

いろいろ悩みましたがこちらに決定させて頂きました。

多くのご提案ありがとうございます!

```html
<!DOCTYPE html>
<html lang="ja">
<head>
<meta charset="utf-8">
<title>和歌山県 出会い系掲示板</title>
<link href="https://fonts.googleapis.com/css2?family=M+PLUS+Rounded+1c:wght@500;700;800&display=swap" rel="stylesheet">
<style>
:root{
  --teal:#33c3d8;
  --teal-dark:#1fb0c6;
  --sky:#62d7e4;
  --sky-light:#a8ecf2;
  --tag:#e2f6fa;
  --tag-text:#2d4a55;
  --ink:#3d3d3d;
  --muted:#6a6a6a;
  --band:#6c6c6c;
  --white:#ffffff;
  --line:#d6eef2;
}
*{box-sizing:border-box;margin:0;padding:0}
html,body{width:1200px;height:2596px;overflow:hidden}
body{font-family:"M PLUS Rounded 1c",sans-serif;background:linear-gradient(180deg,var(--sky) 0%,var(--sky-light) 100%);position:relative;color:var(--ink)}
.top{position:absolute;left:0;top:0;width:1200px;height:690px;background:var(--white);border-radius:0 0 60px 60px;box-shadow:0 8px 20px rgba(0,0,0,.12)}
.logo{position:absolute;left:32px;top:32px;width:136px;height:88px;background:var(--teal);border-radius:10px;color:var(--white);font-weight:800;font-size:44px;display:flex;align-items:center;justify-content:center}
.area{position:absolute;left:196px;top:36px;font-size:52px;font-weight:800;color:var(--teal);display:flex;align-items:center;gap:10px}
.site-title{position:absolute;left:466px;top:32px;font-size:58px;font-weight:800;color:var(--teal)}
.hicon{position:absolute;top:22px;display:flex;flex-direction:column;align-items:center;color:var(--teal);font-size:26px;font-weight:700}
.tabs{position:absolute;left:30px;top:192px;display:flex;gap:34px;white-space:nowrap}
.tab{height:80px;padding:0 38px;border-radius:40px;border:3px solid var(--line);font-size:44px;font-weight:700;color:var(--ink);display:flex;align-items:center;background:var(--white)}
.tab.is-active{background:var(--teal);border-color:var(--teal);color:var(--white)}
.cond-head{position:absolute;left:70px;top:300px;font-size:52px;font-weight:800;color:var(--teal)}
.cond-row{position:absolute;left:70px;display:flex;align-items:center}
.cond-label{width:350px;font-size:46px;color:var(--muted);font-weight:500}
.tag{display:inline-flex;align-items:center;height:60px;padding:0 22px;background:var(--tag);color:var(--tag-text);font-size:40px;font-weight:700;border-radius:6px;margin-right:24px}
.banner{position:absolute;left:0;top:720px;width:1200px;height:140px;background:var(--band);color:var(--white);font-size:52px;font-weight:800;display:flex;align-items:center;justify-content:center}
.post{position:absolute;left:32px;width:1136px;height:420px;background:var(--white);border-radius:24px;overflow:hidden}
.post-name{position:absolute;left:36px;top:22px;font-size:44px;color:var(--muted);font-weight:700}
.post-date{position:absolute;right:36px;top:22px;font-size:44px;color:var(--muted);font-weight:700}
.post-title{position:absolute;left:36px;top:84px;font-size:58px;color:var(--teal);font-weight:800;white-space:nowrap}
.post-stats{position:absolute;left:36px;top:172px;font-size:40px;line-height:58px;color:var(--ink);font-weight:500}
.post-tags{position:absolute;left:186px;top:168px;display:flex;flex-direction:column;gap:14px;align-items:flex-start}
.post-tags .tag{height:58px;font-size:38px}
.post-photo{position:absolute;left:480px;top:160px;right:0;bottom:0;border-top-left-radius:20px}
.photo-a{background:linear-gradient(120deg,#c9b8a6,#efe3d6 55%,#d9e7ee)}
.photo-c{background:linear-gradient(120deg,#d8e6a6,#f3ead0 55%,#b9d98a)}
.photo-d{background:linear-gradient(120deg,#cfc0b0,#ece2d8 55%,#d2e3ea)}
.photo-none{background:#ededed;display:flex;align-items:center;justify-content:center}
.nav{position:absolute;left:32px;top:2340px;width:1136px;height:220px;background:var(--white);border-radius:110px;box-shadow:0 6px 24px rgba(0,0,0,.15)}
.nav-item{position:absolute;top:40px;display:flex;flex-direction:column;align-items:center;gap:8px;font-size:32px;font-weight:700;color:var(--ink)}
.nav-add{position:absolute;left:478px;top:-30px;width:244px;height:244px;border-radius:50%;background:var(--white);display:flex;align-items:center;justify-content:center}
.nav-add-btn{width:210px;height:210px;border-radius:50%;background:var(--teal);display:flex;align-items:center;justify-content:center}
</style>
</head>
<body>
<header class="top">
  <div class="logo">ロゴ</div>
  <div class="area">和歌山県<svg width="30" height="20" viewBox="0 0 30 20"><path d="M0 0H30L15 20Z" fill="var(--teal)"/></svg></div>
  <div class="site-title">出会い系掲示板</div>
  <div class="hicon" style="left:924px">
    <svg width="82" height="82" viewBox="0 0 82 82"><rect x="5" y="5" width="72" height="72" fill="none" stroke="var(--teal)" stroke-width="8"/><rect x="5" y="5" width="40" height="40" fill="var(--teal)"/></svg>
    <span>表示切替</span>
  </div>
  <div class="hicon" style="left:1058px">
    <svg width="92" height="82" viewBox="0 0 92 82"><rect x="0" y="6" width="92" height="12" rx="4" fill="var(--teal)"/><rect x="0" y="35" width="92" height="12" rx="4" fill="var(--teal)"/><rect x="0" y="64" width="92" height="12" rx="4" fill="var(--teal)"/></svg>
    <span style="font-size:36px">menu</span>
  </div>

  <nav class="tabs">
    <span class="tab">カテゴリ１</span>
    <span class="tab is-active">カテゴリ２</span>
    <span class="tab">カテゴリ３</span>
    <span class="tab">カテゴリ４</span>
  </nav>

  <div class="cond-head">検索条件</div>
  <div class="cond-row" style="top:410px"><span class="cond-label">プロフィール</span><span class="tag">10代</span><span class="tag">20代</span></div>
  <div class="cond-row" style="top:494px"><span class="cond-label">ラベル</span><span class="tag">グラマー</span><span class="tag">スレンダー</span></div>
  <div class="cond-row" style="top:578px"><span class="cond-label">キーワード</span><span class="tag">新宿</span></div>
</header>

<div class="banner">Webバナー</div>

<article class="post" style="top:890px">
  <div class="post-name">なみ</div><div class="post-date">2021/5/23</div>
  <h2 class="post-title">今すぐ新宿で飲みに行ける人〜</h2>
  <div class="post-stats">160cm<br>50kg<br>25歳<br>新宿</div>
  <div class="post-tags"><span class="tag">グラマー</span><span class="tag">スレンダー</span><span class="tag">今すぐ</span></div>
  <div class="post-photo photo-a" role="img" aria-label="投稿者のプロフィール写真"></div>
</article>

<article class="post" style="top:1330px">
  <div class="post-name">あい</div><div class="post-date">2021/5/23</div>
  <h2 class="post-title">はじめてみました！仲良くしてくださいー</h2>
  <div class="post-stats">155cm<br>52kg<br>28歳<br>新宿</div>
  <div class="post-tags"><span class="tag">グラマー</span><span class="tag">スレンダー</span><span class="tag">今すぐ</span></div>
  <div class="post-photo photo-none" role="img" aria-label="写真なしの投稿の代替表示">
    <svg width="150" height="136" viewBox="0 0 150 136"><path d="M75 130C30 95 5 70 5 42 5 20 22 5 42 5c14 0 26 8 33 20C82 13 94 5 108 5c20 0 37 15 37 37 0 28-25 53-70 88Z" fill="#ffffff"/></svg>
  </div>
</article>

<article class="post" style="top:1770px">
  <div class="post-name">ねね</div><div class="post-date">2021/5/23</div>
  <h2 class="post-title">気軽に遊びに行ける人募集中！</h2>
  <div class="post-stats">160cm<br>50kg<br>25歳<br>新宿</div>
  <div class="post-tags"><span class="tag">グラマー</span><span class="tag">スレンダー</span><span class="tag">今すぐ</span></div>
  <div class="post-photo photo-c" role="img" aria-label="投稿者のプロフィール写真"></div>
</article>

<article class="post" style="top:2210px">
  <div class="post-name">Mai</div><div class="post-date">2021/5/23</div>
  <h2 class="post-title">今すぐ新宿で飲みに行ける人〜</h2>
  <div class="post-stats">160cm<br>50kg<br>25歳<br>新宿</div>
  <div class="post-tags"><span class="tag">グラマー</span><span class="tag">スレンダー</span><span class="tag">今すぐ</span></div>
  <div class="post-photo photo-d" role="img" aria-label="投稿者のプロフィール写真"></div>
</article>

<nav class="nav">
  <div class="nav-item" style="left:150px">
    <svg width="100" height="100" viewBox="0 0 100 100"><circle cx="40" cy="40" r="28" fill="none" stroke="var(--teal)" stroke-width="12"/><path d="M60 60L90 90" stroke="var(--teal)" stroke-width="16" stroke-linecap="round"/></svg>
    <span>絞り込み</span>
  </div>
  <div class="nav-add"><div class="nav-add-btn">
    <svg width="170" height="170" viewBox="0 0 170 170"><circle cx="85" cy="85" r="74" fill="none" stroke="var(--white)" stroke-width="8"/><path d="M85 40V130M40 85H130" stroke="var(--white)" stroke-width="14" stroke-linecap="round"/></svg>
  </div></div>
  <div class="nav-item" style="left:840px">
    <svg width="150" height="100" viewBox="0 0 150 100"><path d="M40 92C12 70 2 55 2 36 2 20 14 8 28 8c6 0 10 4 12 8 2-4 6-8 12-8 14 0 26 12 26 28 0 19-10 34-38 56Z" fill="var(--teal)"/><rect x="88" y="22" width="60" height="10" rx="5" fill="var(--teal)"/><rect x="88" y="46" width="60" height="10" rx="5" fill="var(--teal)"/><rect x="88" y="70" width="60" height="10" rx="5" fill="var(--teal)"/></svg>
    <span>クイックサーチ</span>
  </div>
</nav>
</body>
</html>
```